WP website design Pine Harbor (Contest)

We need a wordpress design that will incorporate a professional color scheme with company logo in a clean layout. The design needs to consider that this will be developed on a responsive theme. Colors are blue and green of the logo and and an accent color (perhaps very light brown/tan). Client wants a 'modern' look.

Industry/Entity Type

It Company

Font styles to use
Serif
Sans Serif

Colors

Designer to choose colors to be used in the design.

Requirements
Must have
• Navigation: 1) Home; 2) Upcoming Auctions; 3) Past Auctions; 4) About Us; 5) Services; 6) Sellers; 7) Buyers; 8) Contact Us

Site will have slideshow - image is attached. Colors will be those in the logo, blue and green with maybe an accent color. A site the client mentions liking is trevalleauctions.com for the use of color and layout.

Widgets: 1) Featured Properties; 2) Call to action for Sellers 3) Testimonials blog/widget
Nice to have
• use of dropdown menus

```html
<!DOCTYPE html>
<html lang="en">
<head>
<meta charset="utf-8">
<title>Pine Harbor Auction &amp; Real Estate</title>
<link rel="stylesheet" href="https://fonts.googleapis.com/css2?family=Source+Sans+3:wght@400;600;700&family=Arimo:ital,wght@0,400;0,700;1,400;1,700&display=swap">
<style>
:root{
  --green:#0b5a3c;
  --green-dark:#064a30;
  --blue:#1d4a7a;
  --blue-dark:#163d6a;
  --navy:#1b3f6e;
  --text:#333;
  --page:#f9f9f9;
  --bg:#ececec;
  --line:#cfcfcf;
  --foot-text:#eef2f7;
}
*{box-sizing:border-box;margin:0;padding:0}
html,body{width:1145px;height:1200px;overflow:hidden;background:var(--bg)}
body{font-family:"Arimo",Arial,sans-serif;color:var(--text)}
.stage{position:relative;width:1200px;height:1258px;transform:scale(.9542);transform-origin:0 0}
.page{position:absolute;left:103px;top:0;width:995px;height:1258px;background:var(--page);box-shadow:0 0 6px rgba(0,0,0,.12)}
.abs{position:absolute}

/* header */
.site-name{left:126px;top:50px;font-family:"Source Sans 3",sans-serif;font-weight:700;font-size:30px;line-height:36px;color:var(--green);white-space:nowrap}
.contact{left:860px;top:26px;font-size:20px;color:var(--green-dark)}
.contact-row{display:flex;align-items:center;gap:14px;height:30px}
.contact-row.mail{font-size:16px;color:var(--navy)}
.search{left:862px;top:89px;width:220px;height:38px;border-radius:19px;background:linear-gradient(#e2e2e2,#f6f6f6);box-shadow:inset 0 2px 3px rgba(0,0,0,.18)}
.search svg{position:absolute;left:12px;top:10px}

/* nav */
.nav-tab{top:128px;width:20px;height:20px;background:#1a1a1a;border-radius:10px 10px 0 0}
.nav{left:91px;top:144px;width:1019px;height:47px;background:var(--green);display:flex;align-items:center;padding-left:12px}
.nav a{color:#fff;text-decoration:none;font-size:15px;padding:0 22px;line-height:47px;border-right:1px solid #0f6b48;box-shadow:1px 0 0 #053f28}
.nav a:last-child{border:0;box-shadow:none}

/* hero */
.hero{left:116px;top:208px;width:645px;height:362px;background:#ddd;padding:8px}
.hero-photo{width:100%;height:100%;background:linear-gradient(180deg,#8fb8dd 0%,#c9c6a8 35%,#d8d3b3 55%,#5e8a3c 80%,#3f6a2a 100%)}

/* signup */
.signup{left:786px;top:206px;width:311px;height:368px;background:#fff;border-radius:12px;box-shadow:0 0 5px rgba(0,0,0,.15)}
.signup .corner{position:absolute;right:0;top:0}
.panel-title{font-family:"Source Sans 3",sans-serif;font-weight:600;color:var(--navy)}
.signup h2{position:absolute;left:13px;top:32px;font-size:26px}
.signup p{position:absolute;left:15px;top:77px;width:282px;font-size:12px;line-height:18px;color:#333;letter-spacing:.3px}
.field{position:absolute;left:15px;width:282px;height:44px;border-radius:22px;background:linear-gradient(#e6e6e6,#f5f5f5);box-shadow:inset 0 2px 3px rgba(0,0,0,.15);font-size:13px;color:#444;line-height:44px;padding-left:20px}
.btn-sub{position:absolute;left:142px;top:309px;width:152px;height:45px;border-radius:12px;background:var(--green);border:2px solid #fff;box-shadow:0 0 0 1px var(--green);color:#fff;font-family:"Source Sans 3",sans-serif;font-weight:600;font-size:19px;text-align:center;line-height:41px;letter-spacing:.5px}

/* main */
.section-title{font-family:"Source Sans 3",sans-serif;font-weight:600;color:var(--navy)}
.welcome h1{position:absolute;left:112px;top:615px;font-size:26px;letter-spacing:.3px}
.welcome .copy{position:absolute;left:116px;top:660px;width:642px;font-size:12px;line-height:20px;color:#333;text-align:justify}
.copy p+p{margin-top:20px}
.divider-v{left:768px;top:628px;width:1px;height:470px;background:var(--line)}
.divider-dot{left:116px;top:884px;width:644px;border-top:1px dotted #999}
.upcoming h2{position:absolute;left:116px;top:908px;font-size:25px;letter-spacing:.5px}
.lot-title{left:120px;top:951px;font-family:"Source Sans 3",sans-serif;font-weight:700;font-size:16px;color:var(--green);letter-spacing:.3px}
.lot-photo{left:115px;top:982px;width:140px;height:94px;background:linear-gradient(180deg,#a8c8e6 0%,#c8b59a 45%,#6c9a45 70%,#4e8a32 100%)}
.lot-info{left:265px;top:1003px;font-size:12px;line-height:14px;font-style:italic;color:#333}
.lot-info b{font-weight:700}
.pill{top:1076px;height:28px;border-radius:14px;color:#fff;font-size:13px;text-align:center;line-height:24px;border:2px solid #fff;box-shadow:0 0 0 1px #333}
.pill.details{left:605px;width:74px;background:var(--green)}
.pill.photos{left:689px;width:74px;background:var(--blue-dark)}

/* sidebar */
.testimonial{left:800px;top:614px;width:288px;height:202px;background:#fff;border-radius:18px;box-shadow:0 0 5px rgba(0,0,0,.18)}
.testimonial h2{position:absolute;left:15px;top:12px;font-size:27px;letter-spacing:.5px}
.testimonial p{position:absolute;left:15px;top:63px;width:260px;font-size:12px;line-height:20px;color:#444;text-align:justify}
.tail{left:990px;top:814px}
.author{left:999px;top:850px;font-size:13px;color:var(--green);text-decoration:underline}
.news{left:800px;top:878px;width:290px;height:232px;background:#fff;border-radius:14px;box-shadow:0 0 5px rgba(0,0,0,.18)}
.news h2{position:absolute;left:18px;top:14px;font-size:25px;letter-spacing:.5px}
.news-item{position:absolute;left:10px;width:275px}
.news-thumb{position:absolute;left:0;top:0;width:50px;height:50px;background:linear-gradient(#8a6a52,#c59a7a)}
.news-text{position:absolute;left:54px;top:0;width:222px;font-size:12px;line-height:14px;font-style:italic;color:#333}
.news-text b{font-style:normal;color:var(--green);display:block}
.news-date{position:absolute;right:6px;font-size:12px;font-weight:700;font-style:italic;color:var(--navy)}
.news-sep{left:812px;top:1015px;width:266px;border-top:1px dotted #999}

/* footer */
.foot-tab{top:1127px;width:20px;height:20px;background:#1a1a1a;border-radius:10px 10px 0 0}
.footer{left:91px;top:1143px;width:1019px;height:115px;background:var(--blue)}
.footer .info{position:absolute;left:29px;top:14px;color:#fff;font-size:14px;line-height:22px}
.footer .info small{font-size:12.5px}
.foot-name{position:absolute;right:34px;top:42px;font-family:"Source Sans 3",sans-serif;font-weight:700;font-size:24px;line-height:30px;color:var(--foot-text);white-space:nowrap}
</style>
</head>
<body>
<div class="stage">
  <div class="page"></div>

  <header>
    <div class="abs site-name">Pine Harbor Auction &amp; Real Estate</div>

    <div class="abs contact">
      <div class="contact-row">
        <svg width="24" height="20" viewBox="0 0 24 20"><path d="M2 6c0-3 4-4 10-4s10 1 10 4v2h-5V6H7v2H2z" fill="#333"/><rect x="4" y="9" width="16" height="9" rx="1" fill="#333"/><g fill="#fff"><rect x="7" y="11" width="2" height="2"/><rect x="11" y="11" width="2" height="2"/><rect x="15" y="11" width="2" height="2"/><rect x="7" y="14" width="2" height="2"/><rect x="11" y="14" width="2" height="2"/><rect x="15" y="14" width="2" height="2"/></g></svg>
        <span>(555) 014-2290</span>
      </div>
      <div class="contact-row mail">
        <svg width="24" height="16" viewBox="0 0 24 16"><rect width="24" height="16" fill="#222"/><path d="M1 1l11 8 11-8M1 15l8-7M23 15l-8-7" stroke="#fff" stroke-width="1.5" fill="none"/></svg>
        <span>info@pineharborauction.net</span>
      </div>
    </div>
    <div class="abs search">
      <svg width="20" height="20" viewBox="0 0 20 20"><circle cx="8" cy="8" r="6" fill="#fff" stroke="#333" stroke-width="2"/><path d="M12.5 12.5L18 18" stroke="#333" stroke-width="3" stroke-linecap="round"/></svg>
    </div>
  </header>

  <div class="abs nav-tab" style="left:91px"></div>
  <div class="abs nav-tab" style="left:1090px"></div>
  <nav class="abs nav">
    <a>Home</a><a>Upcoming Auctions</a><a>Past Auctions</a><a>About Us</a><a>Services</a><a>Sellers</a><a>Buyers</a><a>Contact Us</a>
  </nav>

  <div class="abs hero">
    <div class="hero-photo" role="img" aria-label="Slideshow photo of a cream-sided family home with a shingle roof, shrubs and garden"></div>
  </div>

  <section class="abs signup">
    <svg class="corner" width="150" height="60" viewBox="0 0 150 60"><path d="M0 0h140a10 10 0 0 1 10 10v30z" fill="#1d4a7a"/><path d="M0 0c40 10 90 25 150 40c-30 5-55 15-60 20C70 30 40 10 0 0z" fill="#e3e3e3"/></svg>
    <h2 class="panel-title">Email sign-up form</h2>
    <p>Lorem ipsum dolor sit amet, consectetuer adipiscing elit. Nam</p>
    <div class="field" style="top:129px">First Name</div>
    <div class="field" style="top:185px">Last Name</div>
    <div class="field" style="top:241px">Email Address</div>
    <div class="btn-sub">Subscribe Now</div>
  </section>

  <section class="welcome">
    <h1 class="section-title">Welcome to Pine Harbor Auction</h1>
    <div class="copy">
      <p><b>In today’s challenging real estate market it takes more than just “a sign and an asking price” to sell your valuable assets. Our job is to bring educated, motivated buyers</b> to your auction in a fair, but competitive environment. This results in signed contracts at market value for the purchase and sale of your real estate.estate market it takes more than just “a sign and an asking price” to sell your valuable assets. Our job is to bring educated, motivated buyers to your auction in a fair, but competitive environment.</p>
      <p>Please explore our site to learn more about our company and our capabilities, or contact us for additional information on how our services can help you to accomplish your goals. This is what we do successfully every day.estate market it takes more than just “a sign and an asking price” to sell your valuable assets. Our job is to bring educated, motivated buyers to your auction in a fair, but competitive environment.</p>
    </div>
  </section>
  <div class="abs divider-v"></div>
  <div class="abs divider-dot"></div>

  <section class="upcoming">
    <h2 class="section-title">Upcoming Auctions</h2>
    <div class="abs lot-title">Incredible Home in Cedar Bluff' exclusive Heron Lake community</div>
    <div class="abs lot-photo" role="img" aria-label="Photo of a lakeside estate with palm trees and a green lawn"></div>
    <div class="abs lot-info">
      <b>Begins:</b>&nbsp; Tuesday, April 23, 2013 at 10:00 AM EDT<br><br>
      <b>Location:</b>&nbsp; Heron Lake Entrance- 1400 N. Lakeview Hwy 9<br>
      Heron Lake Rd (Auction Property)<br>
      Cedar Bluff, FL 30021
    </div>
    <div class="abs pill details">Details</div>
    <div class="abs pill photos">Photos</div>
  </section>

  <aside>
    <div class="abs testimonial">
      <h2 class="panel-title">Clients Testimonial</h2>
      <p>Simply dummy text of the printing and typesetting industry. Lorem Ipsum has been the industry's standard dummy text ever since the 1500s, when an unknown printer took a galley of the industry's standard dummy text ever since the 1500s, when an unknown printer.</p>
    </div>
    <svg class="abs tail" width="34" height="36" viewBox="0 0 34 36"><path d="M0 0l24 32V0z" fill="#fff" stroke="#ddd"/><rect x="1" y="-2" width="22" height="3" fill="#fff"/></svg>
    <div class="abs author">Mara Ellison</div>

    <div class="abs news">
      <h2 class="panel-title">News &amp; Events</h2>
      <div class="news-item" style="top:59px">
        <div class="news-thumb" role="img" aria-label="Author portrait photo"></div>
        <div class="news-text"><b>simply dummy text of the</b>printing and typesetting industry. Lorem Ipsum has been the industry's.</div>
        <div class="news-date" style="top:52px">January 12, 2013</div>
      </div>
      <div class="news-item" style="top:156px">
        <div class="news-thumb" role="img" aria-label="Author portrait photo"></div>
        <div class="news-text" style="left:59px"><b>simply dummy text of the</b>printing and typesetting industry. Lorem Ipsum has been the industry's.</div>
        <div class="news-date" style="top:52px;right:0">January 12, 2013</div>
      </div>
    </div>
    <div class="abs news-sep"></div>
  </aside>

  <div class="abs foot-tab" style="left:91px"></div>
  <div class="abs foot-tab" style="left:1090px"></div>
  <footer class="abs footer">
    <div class="info">
      Halvern Real Estate &amp; Auction Inc.<br>
      4800 Maple Ridge Rd., Fairview KY 40019<br>
      office@halvernauc.com &nbsp;&nbsp;Phone: (555) 017 3381<br>
      <small>Copyright (c) Crestline Real Estate Pine Harbor , Inc. 2014. All Right Reserved</small>
    </div>
    <div class="foot-name">Pine Harbor Auction &amp; Real Estate</div>
  </footer>
</div>
</body>
</html>
```